Business Card needed for Drainora, a growing Septic Service company

Drainora, a growing local septic service company in Pennsylvania, needs updated business cards. We'd like the business card to feature our logo and communicate that we provide Septic Pumping, Installations/Repairs, Restroom Rentals, and 24/7 Emergency Service. The business card should be eye-catching, bold, and clean/simple. We have been in business almost 10 years and would like to expand and update our business brand and image.

Target Market(s)

Residential and Commercial, New and Current Homeowners

Industry/Entity Type

Service

Contact Information for Business Card

Contact on the business card should be: Dale Pruitt Owner & Operator
Phone: 555-555-0187
Email: service@drainora.example
Website: www.drainora.example
Address: 812 Birchwell Lane Easton PA 18042

Font styles to use
Sans Serif

Colors

Designer to choose colors to be used in the design.

Requirements
Must have
• Feature logo on both side of business card.
Nice to have
• We envision the contact information on one side and our services listed on the other side. Utilize the green from the symbol in our logo as part of the design, overall design color scheme should be white, grey, black.

```html
<!DOCTYPE html>
<html lang="en">
<head>
<meta charset="utf-8">
<title>Drainora Business Card</title>
<link rel="stylesheet" href="https://fonts.googleapis.com/css2?family=Arimo:wght@400;700&family=Source+Sans+3:wght@700&family=Open+Sans:wght@400&display=swap">
<style>
  :root {
    --page: #f4f4f4;
    --card-grey: #ebeceb;
    --brand-green: #8dbf2e;
    --mark-green: #1fa83c;
    --ink: #1c1b18;
    --text: #2a2a2a;
    --white: #ffffff;
  }
  * { margin: 0; padding: 0; box-sizing: border-box; }
  html, body {
    width: 1200px; height: 1091px; overflow: hidden;
    background: var(--page);
  }
  .card {
    position: absolute;
    width: 704px; height: 407px;
    border-radius: 18px;
    background: var(--card-grey);
    overflow: hidden;
  }
  .card--front { left: 168px; top: 95px; }
  .card--back { left: 339px; top: 575px; }

  .card__band {
    position: absolute; left: 0; top: 0;
    width: 100%; height: 184px;
  }
  .card--front .card__band { background: var(--brand-green); }
  .card--back .card__band { background: var(--ink); }

  .card__rule {
    position: absolute; left: 0; top: 191px;
    width: 100%; height: 6px;
    background: var(--ink);
  }
  .card__rule-gap {
    position: absolute; left: 0; top: 184px;
    width: 100%; height: 7px;
    background: var(--white);
  }
  .card--back .card__rule-gap { background: var(--card-grey); }

  .brand {
    position: absolute; left: 153px; top: 61px;
    display: flex; align-items: center; gap: 14px;
  }
  .brand__square { width: 70px; height: 70px; }
  .card--front .brand__square { background: var(--mark-green); }
  .card--back .brand__square { background: var(--white); }
  .brand__name {
    font-family: "Arimo", Arial, sans-serif;
    font-weight: 700;
    font-size: 56px;
    letter-spacing: 1px;
    line-height: 1;
  }
  .card--front .brand__name { color: var(--ink); }
  .card--back .brand__name { color: var(--white); }

  .person {
    position: absolute; left: 60px; top: 268px;
    width: 220px; text-align: center;
  }
  .person__name {
    font-family: "Source Sans 3", "Source Sans Pro", sans-serif;
    font-weight: 700; font-size: 36px; line-height: 1;
    color: var(--brand-green);
    letter-spacing: -0.3px;
    white-space: nowrap;
  }
  .person__role {
    font-family: "Open Sans", sans-serif;
    font-size: 21px; color: var(--text);
    margin-top: 6px; letter-spacing: 0.4px;
    white-space: nowrap;
  }

  .contact {
    position: absolute; left: 314px; top: 245px;
    list-style: none;
  }
  .contact__item {
    display: flex; align-items: center;
    height: 29.6px;
    font-family: "Arimo", Arial, sans-serif;
    font-size: 19px; color: var(--text);
    white-space: nowrap;
  }
  .contact__icon { width: 17px; height: 17px; margin-right: 11px; flex: none; }

  .services {
    position: absolute; left: 104px; top: 259px;
    display: grid; grid-template-columns: 246px auto;
    row-gap: 8px; list-style: none;
  }
  .services__item {
    display: flex; align-items: center;
    font-family: "Arimo", Arial, sans-serif;
    font-size: 21px; color: var(--text);
    white-space: nowrap; line-height: 21px;
  }
  .services__item::before {
    content: ""; width: 8px; height: 8px;
    background: var(--brand-green);
    margin-right: 7px; flex: none;
  }
</style>
</head>
<body>

<section class="card card--front">
  <div class="card__band"></div>
  <div class="card__rule-gap"></div>
  <div class="card__rule"></div>
  <div class="brand">
    <span class="brand__square"></span>
    <span class="brand__name">DRAINORA</span>
  </div>
  <div class="person">
    <p class="person__name">DALE PRUITT</p>
    <p class="person__role">Owner &amp; Operator</p>
  </div>
  <ul class="contact">
    <li class="contact__item">
      <svg class="contact__icon" viewBox="0 0 24 24" aria-hidden="true"><path fill="#1c1b18" d="M2 8c0-3 5-5 10-5s10 2 10 5v2h-5V8c-2-1-8-1-10 0v2H2zM6 11h12l3 9H3z"/><g fill="#fff"><rect x="9" y="13" width="2" height="2"/><rect x="13" y="13" width="2" height="2"/><rect x="9" y="16" width="2" height="2"/><rect x="13" y="16" width="2" height="2"/></g></svg>
      555-555-0187
    </li>
    <li class="contact__item">
      <svg class="contact__icon" viewBox="0 0 24 24" aria-hidden="true"><rect x="2" y="5" width="20" height="14" fill="#1c1b18"/><path d="M5 8l7 6 7-6" fill="none" stroke="#fff" stroke-width="2"/></svg>
      service@drainora.example
    </li>
    <li class="contact__item">
      <svg class="contact__icon" viewBox="0 0 24 24" aria-hidden="true"><g fill="none" stroke="#1c1b18" stroke-width="1.6"><circle cx="12" cy="12" r="10"/><ellipse cx="12" cy="12" rx="4.5" ry="10"/><path d="M2 12h20M4 7h16M4 17h16M12 2v20"/></g></svg>
      www.drainora.example
    </li>
    <li class="contact__item">
      <svg class="contact__icon" viewBox="0 0 24 24" aria-hidden="true"><path fill="#1c1b18" d="M12 1a8 8 0 0 0-8 8c0 6 8 14 8 14s8-8 8-14a8 8 0 0 0-8-8zm0 11a3 3 0 1 1 0-6 3 3 0 0 1 0 6z"/></svg>
      812 Birchwell Lane Alderton, ST 00000
    </li>
  </ul>
</section>

<section class="card card--back">
  <div class="card__band"></div>
  <div class="card__rule-gap"></div>
  <div class="card__rule"></div>
  <div class="brand">
    <span class="brand__square"></span>
    <span class="brand__name">DRAINORA</span>
  </div>
  <ul class="services">
    <li class="services__item">Septic Pumping</li>
    <li class="services__item">Restroom Rentals</li>
    <li class="services__item">Installations/Repairs</li>
    <li class="services__item">24/7 Emergency Service</li>
  </ul>
</section>

</body>
</html>
```